Custom Label for Essential Oils Bottle

We are a brand new company who specializes in seeking 100% pure essential oils. You would need to create a label that is similar to the designs attached, but unique to us. Our favorite label design is by quiet harbor blends. We really like how elegant their look is and would like to model that.
We will give the exact text of what we need put into the label to the winner after our favorite design is selected. Also, our logo is attached.
We would like the whole line to follow the same design with minor or tweaks for each scent (different color and text is all).
The label size would be 3" x 1.125" . There will be approximately 60 different oils in our first line but we only need 6 created for our first run.
Attached are the logo designs we really like.
Our first scent will be for a "Lemon" Essential oil bottle so design accordingly. The additional scents will be clove bud , peppermint, sweet orange, rosemary, and eucalyptus.
Thanks so much, and I look forward to seeing your designs!
Sam
Target Market(s)
Women, ages 18-65, wealthy
Industry/Entity Type
It Company

```html
<!DOCTYPE html>
<html lang="en">
<head>
<meta charset="utf-8">
<title>Verra Botanics – Lemon Label</title>
<link rel="stylesheet" href="https://fonts.googleapis.com/css2?family=Montserrat:wght@400;500;700&family=Open+Sans:wght@400&display=swap">
<style>
  :root {
    --page-bg: #ffffff;
    --label-yellow: #fbe27a;
    --label-yellow-light: #fdf0a8;
    --label-yellow-pale: #fff5bf;
    --label-yellow-deep: #f7d65a;
    --label-yellow-warm: #f9dc68;
    --band-yellow: rgba(255, 241, 160, 0.55);
    --ink: #1c1a14;
    --ink-soft: #2e2b22;
  }
  * { margin: 0; padding: 0; box-sizing: border-box; }
  html, body {
    width: 826px;
    height: 1200px;
    overflow: hidden;
    background: var(--page-bg);
  }
  .canvas {
    position: relative;
    width: 826px;
    height: 1200px;
  }
  .label {
    position: absolute;
    left: 40px;
    top: 445px;
    width: 746px;
    height: 310px;
    border-radius: 10px;
    overflow: hidden;
    background: var(--label-yellow);
  }
  .label-pattern {
    position: absolute;
    inset: 0;
    background:
      radial-gradient(ellipse 120px 90px at 420px 70px, var(--label-yellow-light) 0%, transparent 70%),
      radial-gradient(ellipse 110px 110px at 590px 60px, var(--label-yellow-pale) 0%, transparent 70%),
      radial-gradient(ellipse 90px 80px at 690px 150px, var(--label-yellow-light) 0%, transparent 70%),
      radial-gradient(ellipse 130px 90px at 510px 190px, var(--label-yellow-deep) 0%, transparent 70%),
      radial-gradient(ellipse 100px 80px at 640px 250px, var(--label-yellow-light) 0%, transparent 70%),
      radial-gradient(ellipse 110px 70px at 420px 270px, var(--label-yellow-warm) 0%, transparent 70%),
      radial-gradient(ellipse 90px 90px at 40px 250px, var(--label-yellow-light) 0%, transparent 70%),
      radial-gradient(ellipse 80px 70px at 60px 40px, var(--label-yellow-light) 0%, transparent 70%),
      linear-gradient(120deg, var(--label-yellow) 0%, var(--label-yellow-warm) 55%, var(--label-yellow) 100%);
  }
  .scent-band {
    position: absolute;
    left: 0;
    right: 0;
    top: 197px;
    height: 103px;
    background: var(--band-yellow);
  }
  .brand-block {
    position: absolute;
    left: 67px;
    top: 22px;
    width: 290px;
    text-align: center;
    color: var(--ink);
  }
  .brand-name {
    font-family: 'Montserrat', sans-serif;
    font-weight: 700;
    font-size: 42px;
    line-height: 1.05;
    letter-spacing: 0.5px;
  }
  .brand-tagline {
    margin-top: 18px;
    font-family: 'Montserrat', sans-serif;
    font-weight: 500;
    font-size: 16px;
    letter-spacing: 4.2px;
    color: var(--ink-soft);
  }
  .brand-city {
    margin-top: 3px;
    font-family: 'Montserrat', sans-serif;
    font-weight: 400;
    font-size: 14px;
    letter-spacing: 0.5px;
    color: var(--ink-soft);
  }
  .scent-name,
  .scent-purity,
  .scent-volume {
    position: absolute;
    white-space: nowrap;
    color: var(--ink);
  }
  .scent-name {
    left: 183px;
    top: 222px;
    font-family: 'Montserrat', sans-serif;
    font-weight: 700;
    font-size: 26px;
    letter-spacing: 3px;
    color: var(--ink-soft);
  }
  .scent-purity {
    left: 142px;
    top: 254px;
    font-family: 'Open Sans', sans-serif;
    font-size: 13px;
  }
  .scent-volume {
    left: 272px;
    top: 275px;
    font-family: 'Open Sans', sans-serif;
    font-size: 10px;
  }
</style>
</head>
<body>
  <main class="canvas">
    <section class="label">
      <div class="label-pattern" role="img" aria-label="Soft yellow floral swirl and daisy background pattern across the label"></div>
      <div class="scent-band"></div>

      <div class="brand-block">
        <div class="brand-name">Verra<br>Botanics</div>
        <div class="brand-tagline">ESSENTIAL OILS</div>
        <div class="brand-city">NEW YORK</div>
      </div>

      <div class="scent-name">LEMON</div>
      <div class="scent-purity">100% pure essential oils</div>
      <div class="scent-volume">15ml</div>
    </section>
  </main>
</body>
</html>
```